Brindle Forge mens beard oil and balm needs label design.

Brindle Forge is a new Irish start up business that produces gentlemens grooming products. Our first two products will be beard oil and beard balm and we need label designs for both, there will be 3 beard oil products and 3 beard balm products, so label must be editable for ingrediants and product name.
We want the label to include a vintage/oldschool vibe with celtic influences that will appeal to both the older and younger gentleman.

Our bottles are 50ml blue circular glass bottles, dimensions are ht 92.2mm and diam of 37.22mm

Our tins are round aluminium screw on tins, dimensions are 70mm diam and 25mm ht.

label must have Made in Ireland.
Brindle Forge must be prominent in labels.

winning designer will also get to design future products and other designs eg,stickers t shirt promotional material etc etc.

Ingrediants list can be provided when required.
Pictures of bottle and tin are attached.
Any questions feel free to ask.

Looking forward to seeing the designs.

Thanks
Brindle Forge

Beard Oil ingrediants. Harrowmere Ingrediants- Peach Kernel(prunus persica), Grapeseed(vitis vinifera), Sweet almond(prunus dulcis), Golden Jojoba(simmondsia sinensis), Vitamin E. Essential oils- Grapefruit(citrus paradisi), Peppermint(mentha piperita) eucalyptus(eucalyptus globulas), Lime,cold pressed(citrus aurantifolia) Stonebrand - Peach Kernel(prunus persica), Grapeseed(vitis vinifera), Sweet almond(prunus dulcis), Golden Jojoba(simmondsia sinensis), Vitamin E. Essential oils- sandalwood(amyris balsanifera), cedarwood(cedrus atlantica), Pine(pinus sylvestris) Marshlord- Peach Kernel(prunus persica), Grapeseed(vitis vinifera), Sweet almond(prunus dulcis), Golden Jojoba(simmondsia sinensis), Vitamin E. Essential oils- ho leaf(cinnamomum camphora), Bay,west Indian(pimenta racemosa), Cinnamon leaf(cinnamomum zeylanium), Clove bud( eugenia caryophyllus) ps. ingrediants on balms(Tins) will follow. As for now use same ingrediants as above with inclusion of Shea butter, cocoa butter, natural beeswax Balms tins will keep the same pruducts names as beard oils(bottles) eg Harrowmere beard oil and Harrowmere beard balm. Thanks

Target Market(s)

Any man with a beard or mustache 18-80

Industry/Entity Type

Business

Requirements
Must have
• Made in Ireland
Handmade
room for barcode
room for 3 product name variations of both bottle and tin.
eg. Harrowmere, Stonebrand, Tidewall.

Harrowmere ingrediants- Peach Kernel(prunus persica), Grapeseed(vitis vinifera), Sweet almond(prunus dulcis), Golden Jojoba(simmondsia sinensis), Vitamin E.
Essential oils- Grapefruit(citrus paradisi), Peppermint(mentha piperita) eucalyptus(eucalyptus globulas), Lime,cold pressed(citrus aurantifolia)

Essential oil ingrediants which will change from product to product so must be editible from product to product
Nice to have
• Would be nice to see a Brindle design backround or outter edge.

```html
<!DOCTYPE html>
<html lang="en">
<head>
<meta charset="utf-8">
<title>Brindle Forge – Beard Balm &amp; Beard Oil Labels</title>
<link href="https://fonts.googleapis.com/css2?family=Cagliostro&family=Gabriela&family=Yanone+Kaffeesatz:wght@400&family=Mr+De+Haviland&display=swap" rel="stylesheet">
<style>
  :root{
    --page:#ffffff;
    --label-dark:#2e2d2b;
    --label-dark-2:#363432;
    --rim-brown:#6e3f1d;
    --rim-dark:#2a1a0e;
    --brand-red:#d8232a;
    --ink-light:#ecebe8;
    --ink-soft:#d6d4d0;
    --ornament:#3d3b39;
  }
  *{box-sizing:border-box;margin:0;padding:0}
  html,body{width:1200px;height:1000px;overflow:hidden;background:var(--page)}
  body{position:relative;font-family:"Cagliostro",sans-serif;color:var(--ink-light)}
  h2{font-weight:400}

  /* ---------- Tin (balm) labels ---------- */
  .tin-label{
    position:absolute;top:4px;width:400px;height:400px;border-radius:50%;
    background:radial-gradient(circle at 50% 45%,var(--label-dark-2),var(--label-dark) 70%);
    border:12px solid var(--rim-brown);
    box-shadow:0 0 0 2px var(--rim-dark), inset 0 0 0 2px var(--rim-dark);
    text-align:center;overflow:hidden;
  }
  .tin-label--harrowmere{left:0}
  .tin-label--stonebrand{left:400px}
  .tin-label--marshlord{left:800px}

  .brand-name{
    position:absolute;left:0;right:0;color:var(--brand-red);
    font-family:"Cagliostro",sans-serif;font-weight:400;line-height:.95;
  }
  .tin-label .brand-name{top:40px;font-size:44px}

  .flourish{position:absolute;background:var(--ornament);border-radius:40%}
  .tin-label .flourish--left{left:22px;top:160px;width:52px;height:70px}
  .tin-label .flourish--right{right:22px;top:160px;width:52px;height:70px}
  .tin-label .flourish--crest{left:70px;top:6px;width:240px;height:26px;background:var(--rim-brown);opacity:.25}

  .badge-script{position:absolute;font-family:"Mr De Haviland",cursive;font-size:24px;color:var(--ink-soft)}
  .badge-natural{position:absolute;font-family:"Gabriela",serif;font-size:13px;color:var(--ink-soft)}
  .tin-label .badge-script{left:14px;top:104px;transform:rotate(-58deg)}
  .tin-label .badge-natural{right:14px;top:80px;transform:rotate(52deg)}

  .product-name{font-family:"Gabriela",serif;color:var(--ink-light)}
  .product-type{color:var(--brand-red)}
  .tin-label .product-name{position:absolute;left:0;right:0;top:166px;font-size:31px}
  .tin-label .product-type{position:absolute;left:0;right:0;top:206px;font-size:27px}
  .tin-label .directions{position:absolute;left:28px;right:28px;top:240px;font-size:14.5px;line-height:1.2}
  .tin-label .ingredients{
    position:absolute;left:58px;right:58px;top:276px;
    font-family:"Yanone Kaffeesatz",sans-serif;font-size:9px;line-height:10px;color:var(--ink-soft)
  }
  .tin-label .origin{position:absolute;left:0;right:0;top:334px;font-size:17px}
  .tin-label .volume{position:absolute;left:0;right:0;top:358px;font-size:13px}
  .tin-label .shelf-life{position:absolute;left:150px;top:360px}

  .shelf-life{
    display:inline-block;width:18px;height:13px;border:1.5px solid var(--ink-soft);border-radius:2px 2px 4px 4px;
    font-family:"Yanone Kaffeesatz",sans-serif;font-size:7px;line-height:10px;color:var(--ink-soft);text-align:center
  }

  /* ---------- Bottle (oil) labels ---------- */
  .bottle-label{
    position:absolute;height:270px;width:596px;overflow:hidden;
    background:linear-gradient(180deg,var(--label-dark-2),var(--label-dark));
  }
  .bottle-label--stonebrand{left:297px;top:443px}
  .bottle-label--harrowmere{left:0;top:717px;height:283px;width:596px}
  .bottle-label--marshlord{left:600px;top:717px;height:283px;width:600px}

  .bottle-seal{
    position:absolute;width:250px;height:250px;border-radius:50%;
    background:radial-gradient(circle at 50% 45%,var(--label-dark-2),var(--label-dark) 70%);
    border:8px solid var(--rim-brown);box-shadow:0 0 0 2px var(--rim-dark), inset 0 0 0 2px var(--rim-dark);
    text-align:center;overflow:hidden;
  }
  .bottle-label--stonebrand .bottle-seal{left:174px;top:10px}
  .bottle-label--harrowmere .bottle-seal{left:140px;top:14px}
  .bottle-label--marshlord .bottle-seal{left:140px;top:14px}

  .bottle-seal .brand-name{top:30px;font-size:30px}
  .bottle-seal .flourish--left{left:10px;top:110px;width:34px;height:48px}
  .bottle-seal .flourish--right{right:10px;top:110px;width:34px;height:48px}
  .bottle-seal .product-name{position:absolute;left:0;right:0;top:112px;font-size:21px}
  .bottle-seal .product-type{position:absolute;left:0;right:0;top:138px;font-size:19px}
  .bottle-seal .origin{position:absolute;left:0;right:0;top:164px;font-size:13px}
  .bottle-seal .badge-script{left:36px;top:192px;font-size:18px;transform:rotate(-20deg)}
  .bottle-seal .badge-natural{right:32px;top:190px;font-size:10px;transform:rotate(-30deg)}
  .bottle-seal .volume{position:absolute;left:0;right:0;top:190px;font-size:10px}

  .maker-column{
    position:absolute;top:18px;height:240px;writing-mode:vertical-rl;
    font-size:13px;line-height:17px;color:var(--ink-light)
  }
  .bottle-label--stonebrand .maker-column{left:14px}
  .bottle-label--harrowmere .maker-column{left:42px;top:24px}
  .bottle-label--marshlord .maker-column{left:42px;top:24px}

  .bottle-label .shelf-life{position:absolute;left:14px;bottom:10px;transform:rotate(90deg)}
  .bottle-label--harrowmere .shelf-life,.bottle-label--marshlord .shelf-life{left:8px;bottom:12px}

  .usage-column{
    position:absolute;top:12px;height:250px;writing-mode:vertical-rl;transform:rotate(180deg);
    color:var(--ink-light)
  }
  .bottle-label--stonebrand .usage-column{left:442px;width:92px}
  .bottle-label--harrowmere .usage-column{left:438px;width:150px}
  .bottle-label--marshlord .usage-column{left:438px;width:152px}
  .usage-column .directions{font-size:13px;line-height:16px}
  .usage-column .ingredients{margin-right:6px;font-family:"Yanone Kaffeesatz",sans-serif;font-size:13px;line-height:15px;color:var(--ink-soft)}
</style>
</head>
<body>

<!-- Beard balm tins -->
<section class="tin-label tin-label--harrowmere">
  <div class="flourish flourish--crest" role="img" aria-label="Celtic crest ornament"></div>
  <div class="brand-name">Brindle<br>Forge</div>
  <span class="badge-script">Handmade</span>
  <span class="badge-natural">100% natural</span>
  <div class="flourish flourish--left" role="img" aria-label="White filigree scroll ornament"></div>
  <div class="flourish flourish--right" role="img" aria-label="White filigree scroll ornament"></div>
  <h2 class="product-name">harrowmere</h2>
  <p class="product-type">Beard Balm</p>
  <p class="directions">Scoop a pea size amount and rub between palms to soften, apply to beard evenly, style and enjoy.</p>
  <p class="ingredients">Ingredients : Shea butter(Butyrospermum Parkii), Cocoa butter(Theobroma cacao), Peach kernel(Prunus persica), Grapeseed(Vitis vinifera), Golden Jojoba(Simmondsia sinensis), Sweet Almond(Prunus dulcis), Beeswax(Cera flava), Peppermint(Mentha piperita), Eucalyptus(Eucalyptus globulus), Vit E(Tocopherol), Grapefruit(Citrus Paradisi), Lime(Citrus aurantifolia)</p>
  <p class="origin">Made in Ireland</p>
  <span class="shelf-life">12M</span>
  <p class="volume">50ml</p>
</section>

<section class="tin-label tin-label--stonebrand">
  <div class="flourish flourish--crest" role="img" aria-label="Celtic crest ornament"></div>
  <div class="brand-name">Brindle<br>Forge</div>
  <span class="badge-script">Handmade</span>
  <span class="badge-natural">100% natural</span>
  <div class="flourish flourish--left" role="img" aria-label="White filigree scroll ornament"></div>
  <div class="flourish flourish--right" role="img" aria-label="White filigree scroll ornament"></div>
  <h2 class="product-name">stonebrand</h2>
  <p class="product-type">Beard Balm</p>
  <p class="directions">Scoop a pea size amount and rub between palms to soften, apply to beard evenly, style and enjoy.</p>
  <p class="ingredients">Ingredients : Shea butter(Butyrospermum Parkii), Cocoa butter(Theobroma cacao), Peach kernel(Prunus persica), Grapeseed(Vitis vinifera), Golden Jojoba(Simmondsia sinensis), Sweet Almond(Prunus dulcis), Beeswax(Cera flava), Sandalwood(Amyris balsamifera), Cedarwood(Cedrus atlantica), Pine(Pinus sylvestris), Vit E(Tocopherol)</p>
  <p class="origin">Made in Ireland</p>
  <span class="shelf-life">12M</span>
  <p class="volume">50ml</p>
</section>

<section class="tin-label tin-label--marshlord">
  <div class="flourish flourish--crest" role="img" aria-label="Celtic crest ornament"></div>
  <div class="brand-name">Brindle<br>Forge</div>
  <span class="badge-script">Handmade</span>
  <span class="badge-natural">100% natural</span>
  <div class="flourish flourish--left" role="img" aria-label="White filigree scroll ornament"></div>
  <div class="flourish flourish--right" role="img" aria-label="White filigree scroll ornament"></div>
  <h2 class="product-name">marshlord</h2>
  <p class="product-type">Beard Balm</p>
  <p class="directions">Scoop a pea size amount and rub between palms to soften, apply to beard evenly, style and enjoy.</p>
  <p class="ingredients">Ingredients : Shea butter(Butyrospermum Parkii), Cocoa butter(Theobroma cacao), Peach kernel(Prunus persica), Grapeseed(Vitis vinifera), Golden Jojoba(Simmondsia sinensis), Sweet Almond(Prunus dulcis), Beeswax(Cera flava), Ho leaf(Cinnamomum camphora), Bay west Indian(Pimenta racemosa), Vit E(Tocopherol), Cinnamon leaf(Cinnamomum zeylanicum), Clove bud(Eugenia caryophyllus)</p>
  <p class="origin">Made in Ireland</p>
  <span class="shelf-life">12M</span>
  <p class="volume">50ml</p>
</section>

<!-- Beard oil bottles -->
<section class="bottle-label bottle-label--stonebrand">
  <div class="maker-column">Made in limerick Ireland<br>by Brindle Forge.<br>www.brindleforge.ie</div>
  <span class="shelf-life">12M</span>
  <div class="bottle-seal">
    <div class="brand-name">Brindle<br>Forge</div>
    <div class="flourish flourish--left" role="img" aria-label="White filigree scroll ornament"></div>
    <div class="flourish flourish--right" role="img" aria-label="White filigree scroll ornament"></div>
    <h2 class="product-name">stonebrand</h2>
    <p class="product-type">Beard Oil</p>
    <p class="origin">Made in Ireland</p>
    <span class="badge-script">Handmade</span>
    <p class="volume">50ml</p>
    <span class="badge-natural">100% natural</span>
  </div>
  <div class="usage-column">
    <p class="directions">Pour a few drops into palm of your hand apply evenly to beard, style and enjoy</p>
    <p class="ingredients">Ingredients : Peach kernel(Prunus persica), Grapeseed(Vitis vinifera), Sweet Almond(Prunus dulcis), Golden Jojoba (Simmondsia sinensis), Sandalwood(Amyris balsamifera), Cedarwood(Cedrus atlantica), Pine(Pinus sylvestris), Vit E(Tocopherol)</p>
  </div>
</section>

<section class="bottle-label bottle-label--harrowmere">
  <div class="maker-column">Made in limerick Ireland<br>by Brindle Forge.<br>www.brindleforge.ie</div>
  <span class="shelf-life">12M</span>
  <div class="bottle-seal">
    <div class="brand-name">Brindle<br>Forge</div>
    <div class="flourish flourish--left" role="img" aria-label="White filigree scroll ornament"></div>
    <div class="flourish flourish--right" role="img" aria-label="White filigree scroll ornament"></div>
    <h2 class="product-name">harrowmere</h2>
    <p class="product-type">Beard Oil</p>
    <p class="origin">Made in Ireland</p>
    <span class="badge-script">Handmade</span>
    <p class="volume">50ml</p>
    <span class="badge-natural">100% natural</span>
  </div>
  <div class="usage-column">
    <p class="directions">Pour a few drops into palm of your hand apply evenly to beard, style and enjoy</p>
    <p class="ingredients">Ingredients : Peach kernel(Prunus persica), Grapeseed(Vitis vinifera), Sweet Almond(Prunus dulcis), Golden Jojoba (Simmondsia sinensis), Peppermint(Mentha piperita), Eucalyptus(Eucalyptus globulus), Vit E(Tocopherol), Grapefruit(Citrus Paradisi), Lime(Citrus aurantifolia)</p>
  </div>
</section>

<section class="bottle-label bottle-label--marshlord">
  <div class="maker-column">Made in limerick Ireland<br>by Brindle Forge.<br>www.brindleforge.ie</div>
  <span class="shelf-life">12M</span>
  <div class="bottle-seal">
    <div class="brand-name">Brindle<br>Forge</div>
    <div class="flourish flourish--left" role="img" aria-label="White filigree scroll ornament"></div>
    <div class="flourish flourish--right" role="img" aria-label="White filigree scroll ornament"></div>
    <h2 class="product-name">marshlord</h2>
    <p class="product-type">Beard Oil</p>
    <p class="origin">Made in Ireland</p>
    <span class="badge-script">Handmade</span>
    <p class="volume">50ml</p>
    <span class="badge-natural">100% natural</span>
  </div>
  <div class="usage-column">
    <p class="directions">Pour a few drops into palm of your hand apply evenly to beard, style and enjoy</p>
    <p class="ingredients">Ingredients : Peach kernel(Prunus persica), Grapeseed(Vitis vinifera), Sweet Almond(Prunus dulcis), Golden Jojoba(Simmondsia sinensis), Ho leaf(Cinnamomum camphora), Bay west Indian(Pimenta racemosa), Vit E(Tocopherol), Cinnamon leaf(Cinnamomum zeylanicum), Clove bud(Eugenia caryophyllus)</p>
  </div>
</section>

</body>
</html>
```